Prospective Client Marketing Power Point Refresh/Update

My company has been using the attached power point to share with prospective clients. I'd like to have it refreshed with new graphics and style. The color pallet is something we'd like to stay true to. We are looking for your design expertise and ideas to help us update the look of the PP. We work with high wealth clients and want to have this reflect the value we can bring to the table.

Target Market(s)

Wealth Management Clients

Industry/Entity Type

Financial Advisors

Font styles to use
Sans Serif

Colors
0054AA
0677BA
7BADD7
CADEEF
E8F1F8
0094D4
00A9DD
6FCCEA
C7EBF8
E9F6FB

Requirements
Must have
• Updated look
Nice to have
• Fresh graphics

```html
<!DOCTYPE html>
<html lang="en">
<head>
<meta charset="utf-8">
<title>Clearview Advisory – Client Presentation</title>
<link href="https://fonts.googleapis.com/css2?family=Montserrat:wght@400;500;600;700&display=swap" rel="stylesheet">
<style>
:root{
  --navy:#0b3f9c;
  --blue:#0054aa;
  --mid:#0677ba;
  --sky:#0094d4;
  --light:#7badd7;
  --pale:#e8f1f8;
  --ink:#1b1b1f;
  --muted:#4a4a52;
  --canvas:#e3e4e6;
  --white:#ffffff;
}
*{box-sizing:border-box;margin:0;padding:0}
html,body{width:1200px;height:3886px;overflow:hidden}
body{background:var(--canvas);font-family:"Montserrat",sans-serif;color:var(--ink);position:relative}
.slide{position:absolute;left:107px;width:986px;height:555px;background:var(--white);overflow:hidden;box-shadow:0 1px 3px rgba(0,0,0,.12)}
.abs{position:absolute}
.page-no{position:absolute;width:34px;height:34px;border-radius:50%;background:var(--mid);color:#fff;font-size:11px;font-weight:600;display:flex;align-items:center;justify-content:center;right:9px;bottom:9px}
.brand{font-weight:700;color:var(--blue);font-family:"Montserrat",sans-serif;display:flex;align-items:center;gap:6px;line-height:1.05}
.brand-mark{width:12px;height:12px;background:var(--blue);flex:none}
.footer-brand{position:absolute;left:16px;bottom:14px;font-size:12px;width:100px}
.footer-line{position:absolute;left:128px;right:62px;bottom:24px;height:3px;background:linear-gradient(90deg,var(--navy),var(--sky))}
.accent-bar{position:absolute;top:0;height:8px;background:var(--mid)}
.title{position:absolute;font-weight:700;font-size:29px;letter-spacing:.3px;color:var(--ink)}
.photo{position:absolute}

/* slide 2 */
.card{position:absolute;width:280px;height:180px;background:#fff;border-radius:0 0 14px 0;box-shadow:2px 3px 8px rgba(0,0,0,.13)}
.card-badge{position:absolute;left:24px;top:0;width:64px;height:70px}
.card p{position:absolute;left:24px;right:22px;top:90px;font-size:13px;font-weight:600;line-height:20px;color:var(--ink)}

/* slide 3 */
.lede{position:absolute;left:494px;top:30px;width:450px;font-size:12.5px;font-weight:600;line-height:25px}
.donut-label{position:absolute;font-size:12px;line-height:15px;color:var(--ink)}

/* slide 4 */
.pillar{position:absolute;top:100px;width:250px;text-align:center}
.pillar h3{margin-top:232px;font-size:12.5px;font-weight:600;line-height:17px;height:44px}
.pillar p{font-size:9px;line-height:15px;color:var(--muted);text-align:justify;text-align-last:center}

/* slide 5 */
.tile{position:absolute;top:101px;width:207px;height:362px;background:var(--navy)}
.tile-chart{position:absolute;left:5px;right:5px;top:5px;height:170px;background:#fff}
.tile h3{position:absolute;left:14px;right:12px;top:186px;color:#fff;font-size:13px;font-weight:600;line-height:16px}
.tile p{position:absolute;left:14px;right:14px;top:238px;color:#fff;font-size:10px;font-weight:600;line-height:15.5px;text-align:justify}
.dim-title{font-size:8px;font-weight:600;text-decoration:underline;text-align:center;color:var(--navy);margin:10px 0 6px}
.dim-head{font-size:6px;color:var(--mid);margin:4px 14px 3px}
.dim-bar{margin:0 14px 3px;height:10px;font-size:5.5px;color:#fff;padding:2px 4px;line-height:6px}
.dim-bar.eq{background:#2a93a8}
.dim-bar.fi{background:#5a8a24}

/* slide 6 */
.contact{position:absolute;left:706px;font-size:15px;color:var(--ink);display:flex;gap:27px;align-items:flex-start;line-height:30px}
.contact svg{width:14px;height:14px;margin-top:8px;flex:none}
</style>
</head>
<body>

<!-- Slide 01: cover -->
<section class="slide" style="top:86px">
  <svg class="abs" width="986" height="555" viewBox="0 0 986 555" style="left:0;top:0">
    <defs>
      <linearGradient id="coverBlue" x1="0" y1="0" x2="1" y2="1">
        <stop offset="0" stop-color="#0677ba"/><stop offset="1" stop-color="#0b3f9c"/>
      </linearGradient>
      <linearGradient id="coverPhoto" x1="0" y1="0" x2="1" y2="1">
        <stop offset="0" stop-color="#c9ced4"/><stop offset=".5" stop-color="#8f97a3"/><stop offset="1" stop-color="#3c4350"/>
      </linearGradient>
    </defs>
    <polygon points="0,0 735,0 822,150 640,427 0,427" fill="url(#coverPhoto)" role="img" aria-label="Photo of an advisor reviewing documents with a client at a desk"/>
    <polygon points="0,427 640,427 822,150 735,0 828,0 919,156 664,555 0,555" fill="url(#coverBlue)"/>
  </svg>
  <div class="abs brand" style="left:28px;top:16px;background:#fff;padding:10px 12px;font-size:17px;width:160px">Clearview Advisory</div>
  <div class="page-no">01</div>
</section>

<!-- Slide 02: relationship -->
<section class="slide" style="top:718px">
  <div class="accent-bar" style="left:418px;width:150px"></div>
  <h2 class="title" style="left:0;right:0;top:30px;text-align:center">CLEARVIEW ADVISORY RELATIONSHIP</h2>

  <div class="card" style="left:57px;top:86px">
    <svg class="card-badge" viewBox="0 0 64 70"><path d="M0 0H64V48Q64 70 32 70Q0 70 0 48Z" fill="var(--navy)"/><circle cx="32" cy="28" r="10" fill="none" stroke="#fff" stroke-width="2"/><path d="M14 46h10l8 4 14-6" fill="none" stroke="#fff" stroke-width="2"/></svg>
    <p>Providing the highest level of wealth advisory services.</p>
  </div>
  <div class="card" style="left:353px;top:86px">
    <svg class="card-badge" viewBox="0 0 64 70"><path d="M0 0H64V48Q64 70 32 70Q0 70 0 48Z" fill="var(--navy)"/><path d="M16 40l10-14 6 6 6-6 10 14" fill="none" stroke="#fff" stroke-width="2"/></svg>
    <p>We love being a trusted advisor to deliver exceptional service.</p>
  </div>
  <div class="card" style="left:647px;top:86px">
    <svg class="card-badge" viewBox="0 0 64 70"><path d="M0 0H64V48Q64 70 32 70Q0 70 0 48Z" fill="var(--navy)"/><rect x="20" y="16" width="24" height="30" fill="none" stroke="#fff" stroke-width="2"/><path d="M24 38l6-6 4 4 6-8" fill="none" stroke="#fff" stroke-width="2"/></svg>
    <p>There are so many financial decisions that impact multiple areas of an individual's balance sheet exposing you to a</p>
  </div>
  <div class="card" style="left:57px;top:285px">
    <svg class="card-badge" viewBox="0 0 64 70"><path d="M0 0H64V48Q64 70 32 70Q0 70 0 48Z" fill="var(--navy)"/><circle cx="32" cy="32" r="13" fill="none" stroke="#fff" stroke-width="2"/><circle cx="32" cy="30" r="4" fill="none" stroke="#fff" stroke-width="2"/></svg>
    <p>Our goal is to give you the peace of mind that all aspects of your financial picture are being taken care of.</p>
  </div>
  <div class="card" style="left:353px;top:285px">
    <svg class="card-badge" viewBox="0 0 64 70"><path d="M0 0H64V48Q64 70 32 70Q0 70 0 48Z" fill="var(--navy)"/><path d="M32 16l13 5v10q0 11-13 16q-13-5-13-16V21Z" fill="none" stroke="#fff" stroke-width="2"/><rect x="27" y="28" width="10" height="8" fill="none" stroke="#fff" stroke-width="2"/></svg>
    <p>As an independent Registered Investment Advisor, we follow the highest financial standards.</p>
  </div>
  <div class="card" style="left:647px;top:285px">
    <svg class="card-badge" viewBox="0 0 64 70"><path d="M0 0H64V48Q64 70 32 70Q0 70 0 48Z" fill="var(--navy)"/><rect x="18" y="16" width="16" height="26" fill="none" stroke="#fff" stroke-width="2"/><circle cx="40" cy="36" r="8" fill="none" stroke="#fff" stroke-width="2"/></svg>
    <p>We work on a fee-only basis and do not sell commission-based or proprietary products or receive kickbacks of any kind.</p>
  </div>

  <div class="footer-brand brand">Clearview Advisory</div>
  <div class="footer-line"></div>
  <div class="page-no">02</div>
</section>

<!-- Slide 03: services -->
<section class="slide" style="top:1350px">
  <div class="accent-bar" style="left:57px;width:257px"></div>
  <h2 class="title" style="left:57px;top:30px">WHAT DO WE DO?</h2>
  <p class="lede">We have the expertise and experience to provide an exceptional personal advisory relationship.</p>

  <svg class="abs" style="left:0;top:0" width="986" height="555" viewBox="0 0 986 555">
    <g transform="translate(494 317)">
      <circle r="171" fill="none" stroke="var(--mid)" stroke-width="3"/>
      <g transform="rotate(-90)" fill="none" stroke-width="68">
        <circle r="117" stroke="#1a9a7a" stroke-dasharray="91.89 643.27" stroke-dashoffset="0"/>
        <circle r="117" stroke="#2f86d6" stroke-dasharray="91.89 643.27" stroke-dashoffset="-91.89"/>
        <circle r="117" stroke="#2470b8" stroke-dasharray="91.89 643.27" stroke-dashoffset="-183.78"/>
        <circle r="117" stroke="#a35cc2" stroke-dasharray="91.89 643.27" stroke-dashoffset="-275.67"/>
        <circle r="117" stroke="#7a3a9a" stroke-dasharray="91.89 643.27" stroke-dashoffset="-367.56"/>
        <circle r="117" stroke="#f0c530" stroke-dasharray="91.89 643.27" stroke-dashoffset="-459.45"/>
        <circle r="117" stroke="#f29a1e" stroke-dasharray="91.89 643.27" stroke-dashoffset="-551.34"/>
        <circle r="117" stroke="#3bbd9a" stroke-dasharray="91.89 643.27" stroke-dashoffset="-643.23"/>
      </g>
      <circle r="83" fill="#fff"/>
      <circle r="86" fill="none" stroke="rgba(0,0,0,.08)" stroke-width="4"/>
      <g fill="#fff" stroke="var(--mid)" stroke-width="2.5">
        <circle cx="-63" cy="-159" r="6"/><circle cx="65" cy="-159" r="6"/>
        <circle cx="159" cy="-63" r="6"/><circle cx="159" cy="63" r="6"/>
        <circle cx="70" cy="156" r="6"/><circle cx="-63" cy="159" r="6"/>
        <circle cx="-159" cy="63" r="6"/><circle cx="-159" cy="-63" r="6"/>
      </g>
    </g>
  </svg>

  <div class="donut-label" style="left:300px;top:130px;text-align:right;width:130px">Tax Planning &amp;<br>Compliance</div>
  <div class="donut-label" style="left:578px;top:130px">Investment<br>Management</div>
  <div class="donut-label" style="left:673px;top:245px">Executive<br>Compensation<br>&amp; Benefits</div>
  <div class="donut-label" style="left:670px;top:378px">Retirement<br>Planning</div>
  <div class="donut-label" style="left:586px;top:473px">Education</div>
  <div class="donut-label" style="left:350px;top:473px">Insurance</div>
  <div class="donut-label" style="left:180px;top:388px;width:105px;text-align:right">Philanthropy</div>
  <div class="donut-label" style="left:200px;top:245px;width:120px;text-align:right">Cash<br>Management &amp;<br>Budgeting</div>

  <div class="footer-brand brand">Clearview Advisory</div>
  <div class="footer-line"></div>
  <div class="page-no">03</div>
</section>

<!-- Slide 04: philosophy -->
<section class="slide" style="top:1983px">
  <div class="accent-bar" style="left:57px;width:257px"></div>
  <h2 class="title" style="left:57px;top:30px">GUIDING INVESTMENT PHILOSOPHY</h2>

  <div class="pillar" style="left:75px">
    <svg class="abs" style="left:20px;top:0" width="210" height="210" viewBox="0 0 210 210" role="img" aria-label="Photo of an analyst working at a laptop with a calculator"><defs><linearGradient id="p1" x1="0" y1="0" x2="1" y2="1"><stop offset="0" stop-color="#8fae86"/><stop offset="1" stop-color="#3e4a3c"/></linearGradient></defs><circle cx="105" cy="105" r="100" fill="url(#p1)" stroke="var(--blue)" stroke-width="8"/></svg>
    <h3>EMBRACE MARKET PRICING</h3>
    <p>The market is an effective information-processing machine. Each day, the world equity markets process billions of dollars in trades between buyers and sellers – and the real-time information they bring helps set prices.</p>
  </div>
  <div class="pillar" style="left:368px">
    <svg class="abs" style="left:20px;top:0" width="210" height="210" viewBox="0 0 210 210" role="img" aria-label="Photo of hands reviewing financial reports on a desk"><defs><linearGradient id="p2" x1="0" y1="0" x2="1" y2="1"><stop offset="0" stop-color="#c8ccd2"/><stop offset="1" stop-color="#4d535c"/></linearGradient></defs><circle cx="105" cy="105" r="100" fill="url(#p2)" stroke="var(--blue)" stroke-width="8"/></svg>
    <h3>DON'T TRY TO OUTGUESS<br>THE MARKET</h3>
    <p>The market's pricing power works against mutual fund managers who try to outperform through stock pricing or market timing. As evidence, only 23% of US equity mutual funds and 8% of fixed income funds have survived and outperformed their benchmarks over the past 20 years.</p>
  </div>
  <div class="pillar" style="left:658px">
    <svg class="abs" style="left:20px;top:0" width="210" height="210" viewBox="0 0 210 210" role="img" aria-label="Photo of a presenter showing charts to colleagues in a meeting room"><defs><linearGradient id="p3" x1="0" y1="0" x2="1" y2="1"><stop offset="0" stop-color="#d9cdb8"/><stop offset="1" stop-color="#6a5c4c"/></linearGradient></defs><circle cx="105" cy="105" r="100" fill="url(#p3)" stroke="var(--blue)" stroke-width="8"/></svg>
    <h3>RESIST CHASING PAST<br>PERFORMANCE</h3>
    <p>Some investors select mutual funds based on their past returns. Yet, past performance offers little insight into a fund's future returns. For example, most funds in the top quartile (25%) of previous five-year returns did not maintain a top-quartile ranking in the following five years.</p>
  </div>

  <div class="footer-brand brand">Clearview Advisory</div>
  <div class="footer-line"></div>
  <div class="page-no">04</div>
</section>

<!-- Slide 05: efficient markets -->
<section class="slide" style="top:2615px">
  <div class="accent-bar" style="left:57px;width:257px"></div>
  <h2 class="title" style="left:57px;top:30px">THE POWER OF EFFICIENT MARKETS</h2>

  <div class="tile" style="left:57px">
    <div class="tile-chart">
      <svg width="197" height="170" viewBox="0 0 197 170">
        <text x="8" y="16" font-size="5.5" fill="#444" font-family="Montserrat,sans-serif">Growth of a Dollar</text>
        <line x1="8" y1="130" x2="180" y2="130" stroke="#999" stroke-width=".6"/>
        <path d="M8 128 L40 120 L70 110 L100 96 L130 80 L155 60 L175 40 L175 130 L8 130Z" fill="#5fb3c9"/>
        <path d="M8 129 L60 124 L110 114 L150 104 L175 96 L175 130 L8 130Z" fill="#6b9a2e"/>
        <path d="M8 130 L80 127 L175 120 L175 130Z" fill="#1f5a7a"/>
      </svg>
    </div>
    <h3>Let Markets Work for You</h3>
    <p>The financial markets have rewarded long-term investors. People expect a positive return on the capital they supply, and historically, the equity and bond markets have provided growth of wealth that has more than offset inflation.</p>
  </div>
  <div class="tile" style="left:279px">
    <div class="tile-chart">
      <svg width="197" height="170" viewBox="0 0 197 170">
        <text x="8" y="16" font-size="5.5" fill="#444" font-family="Montserrat,sans-serif">Growth of a Dollar</text>
        <line x1="8" y1="130" x2="180" y2="130" stroke="#999" stroke-width=".6"/>
        <path d="M8 128 L40 120 L70 110 L100 96 L130 80 L155 60 L175 40 L175 130 L8 130Z" fill="#5fb3c9"/>
        <path d="M8 129 L60 124 L110 114 L150 104 L175 96 L175 130 L8 130Z" fill="#6b9a2e"/>
        <path d="M8 130 L80 127 L175 120 L175 130Z" fill="#1f5a7a"/>
      </svg>
    </div>
    <h3>Consider the Drivers<br>of Returns</h3>
    <p>There is a wealth of academic research into what drives returns. Expected returns depend on current market prices and expected future cash flows. Investors can use this information to pursue higher expected returns in their portfolios.</p>
  </div>
  <div class="tile" style="left:500px">
    <div class="tile-chart">
      <div class="dim-title">Dimensions of Expected Returns</div>
      <div class="dim-head">EQUITIES</div>
      <div class="dim-bar eq">Company Size</div>
      <div class="dim-bar eq">Relative Price</div>
      <div class="dim-bar eq">Profitability</div>
      <div class="dim-head" style="margin-top:12px">FIXED INCOME</div>
      <div class="dim-bar fi">Term</div>
      <div class="dim-bar fi">Credit</div>
      <div class="dim-bar fi">Currency</div>
    </div>
    <h3>Avoid Market Timing</h3>
    <p>You never know which market segments will out perform from year to year. By holding a globally diversified portfolio, investors are well positioned to seek returns wherever they occur.</p>
  </div>
  <div class="tile" style="left:722px">
    <div class="tile-chart">
      <svg width="197" height="170" viewBox="0 0 197 170">
        <g fill="#9aa0a8"><rect x="8" y="20" width="16" height="3"/><rect x="8" y="40" width="16" height="3"/><rect x="8" y="60" width="16" height="3"/><rect x="8" y="80" width="16" height="3"/><rect x="8" y="100" width="16" height="3"/><rect x="8" y="120" width="16" height="3"/></g>
        <g>
          <rect x="40" y="20" width="14" height="14" fill="#3c6a8c"/><rect x="56" y="20" width="14" height="14" fill="#7fa35c"/><rect x="72" y="20" width="14" height="14" fill="#b0b6bd"/><rect x="88" y="20" width="14" height="14" fill="#5fb3c9"/><rect x="104" y="20" width="14" height="14" fill="#4b3d7a"/><rect x="120" y="20" width="14" height="14" fill="#7fa35c"/><rect x="136" y="20" width="14" height="14" fill="#3c6a8c"/><rect x="152" y="20" width="14" height="14" fill="#b0b6bd"/><rect x="168" y="20" width="14" height="14" fill="#5fb3c9"/>
          <rect x="40" y="36" width="14" height="14" fill="#7fa35c"/><rect x="56" y="36" width="14" height="14" fill="#4b3d7a"/><rect x="72" y="36" width="14" height="14" fill="#5fb3c9"/><rect x="88" y="36" width="14" height="14" fill="#3c6a8c"/><rect x="104" y="36" width="14" height="14" fill="#b0b6bd"/><rect x="120" y="36" width="14" height="14" fill="#5fb3c9"/><rect x="136" y="36" width="14" height="14" fill="#7fa35c"/><rect x="152" y="36" width="14" height="14" fill="#4b3d7a"/><rect x="168" y="36" width="14" height="14" fill="#3c6a8c"/>
          <rect x="40" y="52" width="14" height="14" fill="#b0b6bd"/><rect x="56" y="52" width="14" height="14" fill="#5fb3c9"/><rect x="72" y="52" width="14" height="14" fill="#3c6a8c"/><rect x="88" y="52" width="14" height="14" fill="#7fa35c"/><rect x="104" y="52" width="14" height="14" fill="#5fb3c9"/><rect x="120" y="52" width="14" height="14" fill="#4b3d7a"/><rect x="136" y="52" width="14" height="14" fill="#b0b6bd"/><rect x="152" y="52" width="14" height="14" fill="#3c6a8c"/><rect x="168" y="52" width="14" height="14" fill="#7fa35c"/>
          <rect x="40" y="68" width="14" height="14" fill="#4b3d7a"/><rect x="56" y="68" width="14" height="14" fill="#3c6a8c"/><rect x="72" y="68" width="14" height="14" fill="#7fa35c"/><rect x="88" y="68" width="14" height="14" fill="#b0b6bd"/><rect x="104" y="68" width="14" height="14" fill="#3c6a8c"/><rect x="120" y="68" width="14" height="14" fill="#7fa35c"/><rect x="136" y="68" width="14" height="14" fill="#5fb3c9"/><rect x="152" y="68" width="14" height="14" fill="#b0b6bd"/><rect x="168" y="68" width="14" height="14" fill="#4b3d7a"/>
          <rect x="40" y="84" width="14" height="14" fill="#5fb3c9"/><rect x="56" y="84" width="14" height="14" fill="#b0b6bd"/><rect x="72" y="84" width="14" height="14" fill="#4b3d7a"/><rect x="88" y="84" width="14" height="14" fill="#5fb3c9"/><rect x="104" y="84" width="14" height="14" fill="#7fa35c"/><rect x="120" y="84" width="14" height="14" fill="#3c6a8c"/><rect x="136" y="84" width="14" height="14" fill="#4b3d7a"/><rect x="152" y="84" width="14" height="14" fill="#7fa35c"/><rect x="168" y="84" width="14" height="14" fill="#b0b6bd"/>
          <rect x="40" y="100" width="14" height="14" fill="#3c6a8c"/><rect x="56" y="100" width="14" height="14" fill="#7fa35c"/><rect x="72" y="100" width="14" height="14" fill="#b0b6bd"/><rect x="88" y="100" width="14" height="14" fill="#4b3d7a"/><rect x="104" y="100" width="14" height="14" fill="#b0b6bd"/><rect x="120" y="100" width="14" height="14" fill="#5fb3c9"/><rect x="136" y="100" width="14" height="14" fill="#3c6a8c"/><rect x="152" y="100" width="14" height="14" fill="#5fb3c9"/><rect x="168" y="100" width="14" height="14" fill="#7fa35c"/>
        </g>
      </svg>
    </div>
    <h3>Practice Smart<br>Diversification</h3>
    <p>Holding securities across many market segments can help manage overall risk. But diversifying within your home market may not be enough. Global diversification can broaden your investment universe.</p>
  </div>

  <div class="footer-brand brand">Clearview Advisory</div>
  <div class="footer-line"></div>
  <div class="page-no">05</div>
</section>

<!-- Slide 06: contact -->
<section class="slide" style="top:3246px">
  <svg class="abs" width="986" height="555" viewBox="0 0 986 555" style="left:0;top:0">
    <defs>
      <linearGradient id="closeBlue" x1="0" y1="0" x2="1" y2="1">
        <stop offset="0" stop-color="#0094d4"/><stop offset="1" stop-color="#0b3f9c"/>
      </linearGradient>
      <linearGradient id="closePhoto" x1="0" y1="0" x2="1" y2="1">
        <stop offset="0" stop-color="#d8cfc4"/><stop offset=".6" stop-color="#9c8d7e"/><stop offset="1" stop-color="#4e4a48"/>
      </linearGradient>
    </defs>
    <polygon points="0,0 300,0 470,278 290,459 0,459" fill="url(#closePhoto)" role="img" aria-label="Photo of smiling colleagues meeting at a table"/>
    <polygon points="0,459 290,459 470,278 300,0 557,0 686,278 330,555 0,555" fill="url(#closeBlue)"/>
  </svg>
  <div class="abs brand" style="right:20px;top:26px;font-size:14px;width:110px;text-align:right">Clearview Advisory</div>

  <div class="contact" style="top:225px">
    <svg viewBox="0 0 16 16"><path d="M3 1l3 1 1 3-2 2q2 3 4 4l2-2 3 1 1 3-2 2Q4 14 1 3Z" fill="var(--mid)"/></svg>
    <span>555 010 2090</span>
  </div>
  <div class="contact" style="top:287px">
    <svg viewBox="0 0 16 16"><path d="M8 1a5 5 0 0 1 5 5c0 4-5 9-5 9S3 10 3 6a5 5 0 0 1 5-5Z" fill="var(--mid)"/><circle cx="8" cy="6" r="2" fill="#fff"/></svg>
    <span>4870 Alder Avenue, Suite 210<br>Riverton, OR 97000</span>
  </div>
  <div class="contact" style="top:380px">
    <svg viewBox="0 0 16 16"><rect x="2" y="6" width="12" height="8" rx="1" fill="var(--mid)"/><rect x="5" y="2" width="6" height="5" fill="var(--mid)"/><rect x="5" y="9" width="6" height="2" fill="#fff"/></svg>
    <span>555 010 6205</span>
  </div>
  <div class="contact" style="top:442px">
    <svg viewBox="0 0 16 16"><rect x="1" y="3" width="14" height="10" fill="var(--mid)"/><path d="M1 3l7 6 7-6" fill="none" stroke="#fff" stroke-width="1.2"/></svg>
    <span>www.clearviewadvisory.com</span>
  </div>
  <div class="page-no">06</div>
</section>

</body>
</html>
```